Wordpress Redesign Project

Our website needs to become amazing. Because now it's not. The homepage especially does not actively convey what we do in an elegant way. We would want a minimalist redesign of www.plovK.com to look more like:

http://vantorelliworks.com/
http://www.quorvane.com/en-us/quorvaneflux.html
http://www.bramu.com/

It needs to work on Wordpress and be easily uploaded.

We also need an inside page of case studies (currently http://www.plovk.com/social-media-clients/) that plays the video in a larger pop-up screen .

Target Market(s)

Social Media Professionals, Creative and Advertising Agencies, Event marketing professionals

Industry/Entity Type

Media

```html
<!DOCTYPE html>
<html lang="en">
<head>
<meta charset="utf-8">
<title>plovK – Creating Brand Champions</title>
<link href="https://fonts.googleapis.com/css2?family=Yanone+Kaffeesatz:wght@300;400;500&family=Arimo:wght@400&display=swap" rel="stylesheet">
<style>
:root{
  --pink:#dd178b;
  --pink-deep:#b8116f;
  --pink-dark:#a50f62;
  --page:#f3f3f3;
  --card:#ffffff;
  --ink:#3a3a3a;
  --rule:#e2e2e2;
  --head-font:"Yanone Kaffeesatz",sans-serif;
  --body-font:"Arimo",Arial,sans-serif;
}
*{box-sizing:border-box;margin:0;padding:0}
html,body{width:1200px;height:1160px;overflow:hidden}
body{position:relative;background:var(--page);font-family:var(--body-font);color:var(--ink)}
.abs{position:absolute}
.backdrop{left:0;top:0}
.brand{left:210px;top:8px;display:flex;align-items:center;gap:8px}
.brand-mark{width:62px;height:62px;background:var(--pink);border-radius:14px}
.brand-name{font-family:var(--head-font);font-weight:500;font-size:40px;color:var(--pink);line-height:1}
.tagline{left:360px;top:30px;font-family:var(--head-font);font-size:21px;color:var(--pink);letter-spacing:1px}
.demo-tab{left:856px;top:0;width:128px;height:19px;background:#ececec;clip-path:polygon(0 100%,22px 0,100% 0,100% 100%);font-family:var(--head-font);font-size:12px;color:var(--pink);text-align:right;padding:3px 34px 0 0}
.nav{right:216px;font-family:var(--head-font);font-size:14px;color:#fff;white-space:nowrap}
.nav span+span::before{content:"•";margin:0 7px;font-size:10px;vertical-align:2px}
.nav-top{top:38px}.nav-main{top:58px}
.hero{left:216px;top:86px;width:768px;height:307px;background:#fff;clip-path:polygon(0 0,100% 0,100% 240px,654px 100%,0 100%)}
.hero-photo{left:6px;top:5px;width:757px;height:296px;background:linear-gradient(120deg,#d9d9d9,#b4b4b4 45%,#e6e6e6 80%,#cfcfcf);clip-path:polygon(0 0,100% 0,100% 229px,640px 100%,0 100%)}
.caption{font-family:var(--head-font);font-size:16.5px;color:#fff;background:var(--pink);white-space:nowrap;text-align:center}
.caption-1{left:589px;top:204px;width:368px;height:30px;line-height:30px}
.caption-2{left:742px;top:237px;width:215px;height:30px;line-height:30px}
.hero-arrows{left:936px;top:360px}
.card{background:var(--card)}
.about{left:216px;top:417px;width:768px;height:287px;box-shadow:0 6px 14px rgba(0,0,0,.06)}
.section-title{font-family:var(--head-font);font-size:17px;color:var(--pink);font-weight:400}
.about .section-title{left:16px;top:13px}
.about-thumb{left:18px;top:43px;width:115px;height:90px;background:radial-gradient(circle at 30% 50%,#1b1b1b 40%,#5b1b4a 70%,#a02278);clip-path:polygon(0 0,100% 0,100% 60px,70px 100%,0 100%)}
.about-copy{left:149px;top:44px;width:592px;font-size:10.5px;line-height:14.4px}
.more-corner{left:708px;top:99px}
.tiles{left:216px;top:570px;width:768px;display:flex}
.tile{width:192px}
.tile-photo{height:103px}
.tile-label{height:31px;line-height:31px;text-align:center;color:#fff;font-size:10.5px}
.article-title{left:216px;top:726px;font-family:var(--head-font);font-size:16px;font-weight:400;color:var(--pink);white-space:nowrap}
.article-copy{left:217px;top:750px;width:510px;font-size:10.4px;line-height:14.4px}
.article-copy a{color:var(--pink);text-decoration:none}
.video{left:216px;top:820px;width:240px;height:175px;background:#111}
.video-frame{left:0;top:18px;width:240px;height:139px;background:linear-gradient(135deg,#6f6a84,#9c8d88 50%,#c8b7a5)}
.why{left:478px;top:820px;width:240px;height:176px;padding:18px 18px 0}
.why .section-title{font-size:15.5px;margin-bottom:4px}
.why p{font-size:10.4px;line-height:14.4px}
.blog{left:743px;top:721px;width:241px;height:275px;padding:14px 16px 0 16px}
.blog .section-title{padding-left:20px;margin-bottom:11px}
.blog ul{list-style:none}
.blog li{position:relative;padding:0 0 6px 15px;margin-bottom:8px;border-bottom:1px solid var(--rule);font-size:10.2px;line-height:14.4px;height:35px}
.blog li:last-child{border-bottom:0}
.blog li::before{content:"";position:absolute;left:2px;top:4px;width:5px;height:5px;border-right:1.5px solid #222;border-top:1.5px solid #222;transform:rotate(45deg)}
.blog li.active{color:var(--pink)}
.blog li.active::before{border-color:var(--pink)}
.client{top:1028px;width:112px;height:66px;background:#fff;border:3px solid #e4e4e4;border-radius:3px;display:flex;align-items:center;justify-content:center;font-family:var(--head-font);font-size:22px;font-weight:500}
.carousel-btn{left:699px;width:21px;height:20px}
.cta{left:743px;top:1026px;width:241px;height:68px;background:var(--pink);border-radius:4px;padding:14px 0 0 39px;font-family:var(--head-font);font-size:15.5px;line-height:18px;color:#fff}
.footer{left:0;top:1116px;width:1200px;height:44px;background:var(--pink);color:#fff;font-size:10.5px;padding:13px 0 0 216px}
</style>
</head>
<body>

<svg class="abs backdrop" width="1200" height="470" viewBox="0 0 1200 470" aria-hidden="true">
  <polygon points="0,392 210,272 210,80 552,80 688,0 1200,0 1200,462 0,462" fill="#dd178b"/>
  <rect x="210" y="0" width="342" height="80" fill="#f7f7f7"/>
  <polygon points="552,80 688,0 552,0" fill="#f7f7f7"/>
</svg>

<div class="abs brand"><div class="brand-mark"></div><div class="brand-name">plovK</div></div>
<div class="abs tagline">CREATING BRAND CHAMPIONS</div>

<div class="abs demo-tab">REQUEST A DEMO</div>
<nav class="abs nav nav-top"><span>HOME</span><span>CONTACTUS</span><span>VIA RSS</span></nav>
<nav class="abs nav nav-main"><span>ABOUT US</span><span>SOLUTIONS</span><span>NEWS</span><span>RESOURCE</span><span>OUR WORK</span><span>SOCIAL BLOG</span></nav>

<section class="abs hero">
  <div class="abs hero-photo" role="img" aria-label="Smiling business team in suits"></div>
</section>
<div class="abs caption caption-1">LOREM IPSUM IS SIMPLY DUMMY TEXT OF THE PRINTING AND TYPESETTI</div>
<div class="abs caption caption-2">PRINTING AND TYPESETTING INDUSTRY.</div>
<svg class="abs hero-arrows" width="32" height="24" viewBox="0 0 32 24" aria-hidden="true">
  <polyline points="10,2 2,12 10,22" fill="none" stroke="#fff" stroke-width="2"/>
  <polyline points="22,2 30,12 22,22" fill="none" stroke="#fff" stroke-width="2"/>
</svg>

<section class="abs card about">
  <h2 class="abs section-title">WHAT WE DO</h2>
  <div class="abs about-thumb" role="img" aria-label="Car brand display at a live event"></div>
  <p class="abs about-copy">plovK is in the business of creating brand champions.&nbsp; We help get consumers to put your branded content into their Friendwall News Feed and Chirpline stream while attending live events. It is product placement in social media and the most scalable form of word-of-mouth advertising. We facilitate the posts by providing a platform that connects to photobooths, roving photographers, Like boxes, games and buzz walls and generates automated social media posts. It is a significant leverage on event guest engagement, drives social media impressions and extends the brand's audience.</p>
  <svg class="abs more-corner" width="44" height="44" viewBox="0 0 44 44" aria-hidden="true">
    <polygon points="44,0 44,44 0,44" fill="#dd178b"/>
    <path d="M38 33H26M32 27V39" stroke="#fff" stroke-width="1.6"/>
  </svg>
</section>

<div class="abs tiles">
  <div class="tile"><div class="tile-photo" role="img" aria-label="Costumed guests at a gaming event" style="background:linear-gradient(135deg,#4f7fb0,#c8453a 50%,#3f8a3a)"></div><div class="tile-label" style="background:#dd178b">AMPLIFY YOUR EVENTS</div></div>
  <div class="tile"><div class="tile-photo" role="img" aria-label="Skiers posing on a snowy mountain" style="background:linear-gradient(180deg,#9a9a9a,#5e5e5e 55%,#d6d6d6)"></div><div class="tile-label" style="background:#b8116f">CONNECT VENUES</div></div>
  <div class="tile"><div class="tile-photo" role="img" aria-label="Cheering crowd at a live event" style="background:linear-gradient(180deg,#7a7a7a,#3a3a3a)"></div><div class="tile-label" style="background:#a50f62;border-right:1px solid #8e0c55">IN ACTION</div></div>
  <div class="tile"><div class="tile-photo" role="img" aria-label="Excited group of young fans" style="background:linear-gradient(180deg,#555,#2a2a2a)"></div><div class="tile-label" style="background:#a70e65">SOCIAL SOLUTIONS</div></div>
</div>

<h2 class="abs article-title">AUREVIA AMPLIFIES GRAND CIRCUIT WITH RFID USING SOCIAL MEDIA TECHNOLOGY</h2>
<p class="abs article-copy">The video below shows how auto brands are connecting auto show and lifestyle event guests directly to social media using RFID and NFC Technology. These activations are fun for guests and expand the potential audience for social engagement beyond attendees to include their social network friends.<br><a href="#">Watch Video Below to see it in action!</a></p>

<div class="abs video">
  <div class="abs video-frame" role="img" aria-label="Video still of a guest at a racing event"></div>
  <svg class="abs" style="left:0;top:0" width="240" height="175" viewBox="0 0 240 175" aria-hidden="true">
    <rect x="99" y="63" width="42" height="28" rx="5" fill="#1a1a1a" opacity=".85"/>
    <polygon points="115,70 115,84 127,77" fill="#fff"/>
    <rect x="0" y="157" width="240" height="18" fill="#1b1b1b"/>
    <rect x="0" y="156" width="240" height="3" fill="#c81e1e"/>
    <polygon points="10,163 10,171 16,167" fill="#999"/>
    <text x="46" y="170" font-size="6" fill="#aaa" font-family="Arial,sans-serif">0:00</text>
  </svg>
</div>

<section class="abs card why">
  <h3 class="section-title">WHY CONSUMER BRANDS LOVE PLOVK</h3>
  <p>Turn live audiences into brand champions. Global consumer brands engage plovK to leverage an asset they encounter at every event: attendees. Event guests have social network audiences who like and trust them. plovK solutions facilitate participation and enable easy distribution of branded content to friends. Fun for guests. Amplification for brands.</p>
</section>

<aside class="abs card blog">
  <h3 class="section-title">SOCIAL BLOG</h3>
  <ul>
    <li class="active">What does Hallmoor do for Social Media Today? [Video Blog]</li>
    <li>Who is using Social Media? Young? Old? Both? Yes!</li>
    <li>Social Reach Summit Interview: Marit Olvenhaar of Skyvaal</li>
    <li>RFID Connects Social Media to the Real World, Instantly</li>
    <li>Adding Experiential Social Media to Events [Video Interview - Torvane]</li>
  </ul>
</aside>

<div class="abs client" style="left:216px;color:#d81e25">Pixelmoor</div>
<div class="abs client" style="left:338px;color:#555">TORVANE</div>
<div class="abs client" style="left:459px;color:#3d1f83">Cocobrin</div>
<div class="abs client" style="left:581px;color:#333">lumadeal</div>

<svg class="abs carousel-btn" style="top:1036px" viewBox="0 0 21 20" aria-hidden="true"><rect width="21" height="20" fill="#dd178b"/><polyline points="8,5 13,10 8,15" fill="none" stroke="#fff" stroke-width="2.4"/></svg>
<svg class="abs carousel-btn" style="top:1062px" viewBox="0 0 21 20" aria-hidden="true"><rect width="21" height="20" fill="#1b1b1b"/><polyline points="13,5 8,10 13,15" fill="none" stroke="#fff" stroke-width="2.4"/></svg>

<a class="abs cta">PLOVK IS A FRIENDWALL PREFERRED<br>MARKETING DEVELOPER
  <svg width="22" height="14" viewBox="0 0 22 14" style="vertical-align:-2px" aria-hidden="true"><polyline points="2,1 8,7 2,13" fill="none" stroke="#fff" stroke-width="3"/><polyline points="11,1 17,7 11,13" fill="none" stroke="#fff" stroke-width="3"/></svg>
</a>

<footer class="abs footer">© Copyright 2013 plovK</footer>

</body>
</html>
```